Business Card Design For A Renovation Contractor Company

We need a business card for a new company based in Singapore, our company name is "KT Planora". We are a renovation contractor that builds designs into reality. We build more of F&B restaurants, retail stores and commercial offices. We work very closely with designers. The final design should communicate to our client that we are a company that you can trust, that will plan and complete your project without giving you a headache. I like my client to remember my company as "KT". The beauty of SIMPLE is important.

Industry/Entity Type

Contractor

Requirements
Nice to have
• Black or Red base

```html
<!DOCTYPE html>
<html lang="en">
<head>
<meta charset="utf-8">
<title>KT Planora – Business Cards</title>
<link rel="stylesheet" href="https://fonts.googleapis.com/css2?family=Open+Sans:wght@400;700&family=Questrial&display=swap">
<style>
  :root {
    --stage: #ebe6de;
    --card-white: #ffffff;
    --card-red: #d42027;
    --card-black: #000000;
    --accent-red: #d42027;
    --ink: #111111;
    --ink-soft: #444444;
    --disc-white: #f1f0f0;
    --disc-red: #c4222a;
    --disc-black: #2e2622;
    --rule: #b9b9b9;
    --paper: #ffffff;
  }
  * { box-sizing: border-box; margin: 0; padding: 0; }
  html, body { width: 1200px; height: 714px; overflow: hidden; }
  body { background: var(--stage); position: relative; font-family: "Open Sans", Arial, sans-serif; }

  .card {
    position: absolute;
    width: 546px;
    height: 313px;
    border-radius: 26px;
    overflow: hidden;
  }
  .card--front { left: 36px; top: 29px; background: var(--card-white); border: 1px solid #555; }
  .card--red   { left: 611px; top: 33px; background: var(--card-red); }
  .card--black { left: 328px; top: 364px; background: var(--card-black); }

  .backdrop-disc {
    position: absolute;
    width: 288px; height: 288px;
    border-radius: 50%;
  }
  .card--front .backdrop-disc { left: 265px; top: 18px; background: var(--disc-white); }
  .card--red .backdrop-disc   { left: 259px; top: 10px; background: var(--disc-red); }
  .card--black .backdrop-disc { left: 261px; top: 12px; background: var(--disc-black); }

  .holder-name {
    position: absolute; left: 27px; top: 52px;
    font-weight: 700; font-size: 21px; color: var(--ink); letter-spacing: 0.2px;
  }
  .holder-title {
    position: absolute; left: 27px; top: 82px;
    font-size: 16px; color: var(--accent-red);
  }
  .web-address {
    position: absolute; left: 28px; top: 289px; transform: translateY(-100%);
    font-size: 16px; letter-spacing: 3.2px; color: var(--ink-soft);
  }
  .web-address .web-name { color: var(--accent-red); font-weight: 700; }

  .contact-list {
    position: absolute; left: 338px; top: 176px;
    list-style: none; font-size: 13.5px; color: var(--ink-soft); line-height: 19px;
  }
  .contact-list li { display: flex; align-items: flex-start; margin-bottom: 6px; }
  .contact-list svg { width: 12px; height: 12px; margin: 3px 8px 0 0; flex: none; fill: var(--accent-red); }

  .wordmark {
    position: absolute; left: 29px; top: 216px;
    font-family: "Questrial", Arial, sans-serif;
    font-size: 50px; line-height: 1; color: var(--paper); letter-spacing: -0.5px;
  }
  .wordmark-rule {
    position: absolute; left: 29px; top: 266px; width: 298px; height: 1px; background: var(--rule);
  }
  .tagline {
    position: absolute; left: 44px; top: 267px;
    font-family: "Questrial", Arial, sans-serif;
    font-size: 19px; color: var(--paper); letter-spacing: 1px; white-space: nowrap;
  }
</style>
</head>
<body>

  <section class="card card--front" aria-label="Card front">
    <div class="backdrop-disc"></div>
    <p class="holder-name">YOUR NAME</p>
    <p class="holder-title">TITLE</p>
    <ul class="contact-list">
      <li>
        <svg viewBox="0 0 12 12"><path d="M0 4 L6 0 L12 4 Z M1 5h10v1.5H1z M1 7.5h10V9H1z M1 10h10v2H1z"/></svg>
        <span>Street Name, City Name<br>State Zip Code</span>
      </li>
      <li>
        <svg viewBox="0 0 12 12"><circle cx="6" cy="6" r="5.5" fill="none" stroke="#d42027" stroke-width="1.2"/><path d="M4 3 Q3 6 6 9 L7.5 8 L6.5 6.5 L5.8 7 Q4.8 5.8 5.2 4.5 L6 4.2 L5.4 2.6 Z"/></svg>
        <span>123-456-0789</span>
      </li>
      <li>
        <svg viewBox="0 0 12 12"><rect x="2.5" y="0" width="7" height="12" rx="1.2"/><rect x="3.8" y="1.5" width="4.4" height="4" fill="#fff"/><rect x="3.8" y="7" width="4.4" height="3.5" fill="#fff"/></svg>
        <span>123-456-0789</span>
      </li>
      <li>
        <svg viewBox="0 0 12 12"><path d="M0 4 L6 0 L12 4 V12 H0 Z"/><path d="M1 4.5 L6 8 L11 4.5" fill="none" stroke="#fff" stroke-width="1"/></svg>
        <span>info@ktplanora.com</span>
      </li>
    </ul>
    <p class="web-address">www.<span class="web-name">ktplanora</span>.com</p>
  </section>

  <section class="card card--red" aria-label="Card back, red">
    <div class="backdrop-disc"></div>
    <p class="wordmark">KT Planora</p>
    <div class="wordmark-rule"></div>
    <p class="tagline">your project, built with care</p>
  </section>

  <section class="card card--black" aria-label="Card back, black">
    <div class="backdrop-disc"></div>
    <p class="wordmark">KT Planora</p>
    <div class="wordmark-rule"></div>
    <p class="tagline">your project, built with care</p>
  </section>

</body>
</html>
```